business card for KestrelLine Construction
need a tag line (here to meet your needs)?
business card for KestrelLine Construction -
Creative Brief
Simple
Lorcan Whitlaney
Foreman
New Jersey or servicing north jersey
info@Kestrel-Line.com
www.Kestrel-Line.com
fully licensed fully insured
logo. residential commercial. 24hr emergency service. specializing in: *roofs *chimneys *masonry *gutters
logo. pic of workvan with logo Notes:________________________________________________________________________________________

```html
<!DOCTYPE html>
<html lang="en">
<head>
<meta charset="utf-8">
<title>KestrelLine Construction – Business Card</title>
<link rel="stylesheet" href="https://fonts.googleapis.com/css2?family=Arimo:wght@400;700&display=swap">
<style>
  :root {
    --navy-deep: #13206a;
    --navy: #1f3596;
    --orange: #f39a1e;
    --white: #ffffff;
    --ink-blue: #233a9e;
    --backdrop: #e9e6e1;
    --muted: #c9d2f3;
  }
  * { margin: 0; padding: 0; box-sizing: border-box; }
  html, body { width: 1200px; height: 852px; overflow: hidden; }
  body {
    background: var(--backdrop);
    font-family: "Arimo", Arial, sans-serif;
    position: relative;
  }
  .card {
    position: absolute;
    width: 540px;
    height: 320px;
    border-radius: 18px;
    overflow: hidden;
    box-shadow: 0 10px 24px rgba(0,0,0,.25);
  }
  .card--front-left { left: 70px; top: 110px; }
  .card--front-right { left: 590px; top: 420px; }
  .card__bg { position: absolute; inset: 0; width: 100%; height: 100%; }

  .contact { position: absolute; top: 26px; color: var(--white); }
  .card--front-left .contact { left: 30px; }
  .card--front-right .contact { right: 30px; text-align: right; }

  .contact__name { font-weight: 700; font-size: 18px; }
  .contact__role { font-size: 13px; color: var(--muted); margin-top: 2px; }
  .contact__area { font-size: 14px; margin-top: 42px; }
  .contact__list { list-style: none; margin-top: 8px; font-size: 14px; line-height: 21px; }
  .contact__list li { display: flex; align-items: center; gap: 8px; }
  .card--front-right .contact__list li { justify-content: flex-end; }
  .icon { width: 14px; height: 14px; flex: none; }
  .contact__special { margin-top: 12px; font-size: 14px; font-weight: 700; }
  .contact__trades { font-size: 14px; font-weight: 700; margin-top: 4px; white-space: nowrap; }

  .brand {
    position: absolute;
    top: 112px;
    width: 220px;
    text-align: center;
  }
  .card--front-left .brand { right: 6px; }
  .card--front-right .brand { left: 14px; }
  .brand__name {
    font-weight: 700;
    font-size: 27px;
    line-height: 30px;
    color: var(--ink-blue);
  }
  .brand__tagline {
    margin-top: 10px;
    font-size: 10px;
    color: var(--orange);
    font-weight: 700;
  }
</style>
</head>
<body>

<svg width="0" height="0" style="position:absolute">
  <defs>
    <linearGradient id="navyFill" x1="0" y1="0" x2="1" y2="1">
      <stop offset="0" stop-color="#2b43ad"/>
      <stop offset="1" stop-color="#101a5c"/>
    </linearGradient>
    <symbol id="icon-phone" viewBox="0 0 16 16">
      <path d="M4 1.5l2.2 2.6-1.3 1.6c.8 1.9 2.3 3.4 4.2 4.2l1.6-1.3 2.6 2.2-1.4 2.4C7 12.6 3.4 9 1.6 2.9z" fill="currentColor"/>
    </symbol>
    <symbol id="icon-at" viewBox="0 0 16 16">
      <circle cx="8" cy="8" r="6.5" fill="none" stroke="currentColor" stroke-width="1.6"/>
      <circle cx="8" cy="8" r="2.3" fill="none" stroke="currentColor" stroke-width="1.6"/>
    </symbol>
    <symbol id="icon-web" viewBox="0 0 16 16">
      <circle cx="8" cy="8" r="6.5" fill="none" stroke="currentColor" stroke-width="1.4"/>
      <path d="M1.5 8h13M8 1.5c-3 3.5-3 9.5 0 13M8 1.5c3 3.5 3 9.5 0 13" fill="none" stroke="currentColor" stroke-width="1.2"/>
    </symbol>
  </defs>
</svg>

<!-- Layout A: blue panel left -->
<section class="card card--front-left">
  <svg class="card__bg" viewBox="0 0 540 320" preserveAspectRatio="none" aria-hidden="true">
    <rect width="540" height="320" fill="url(#navyFill)"/>
    <path d="M326,0 C286,100 286,220 318,320" fill="none" stroke="var(--orange)" stroke-width="10"/>
    <path d="M340,0 C300,100 300,220 332,320 L540,320 L540,0 Z" fill="var(--white)"/>
  </svg>
  <div class="contact">
    <p class="contact__name">Lorcan Whitlaney</p>
    <p class="contact__role">Foreman</p>
    <p class="contact__area">Servicing North Jersey</p>
    <ul class="contact__list">
      <li><svg class="icon"><use href="#icon-phone"/></svg>(T)1-888-555-0142</li>
      <li><svg class="icon"><use href="#icon-phone"/></svg>201-555-0187</li>
      <li><svg class="icon"><use href="#icon-at"/></svg>info@Kestrel-Line.com</li>
      <li><svg class="icon"><use href="#icon-web"/></svg>www.Kestrel-Line.com</li>
    </ul>
    <p class="contact__special">Specializing in :</p>
    <p class="contact__trades">roofs / chimneys / masonry / gutters</p>
  </div>
  <div class="brand">
    <p class="brand__name">KestrelLine<br>Construction</p>
    <p class="brand__tagline">Residential &amp; Commercial... 24hr emergency service.</p>
  </div>
</section>

<!-- Layout B: blue panel right -->
<section class="card card--front-right">
  <svg class="card__bg" viewBox="0 0 540 320" preserveAspectRatio="none" aria-hidden="true">
    <rect width="540" height="320" fill="url(#navyFill)"/>
    <path d="M214,0 C254,100 254,220 222,320" fill="none" stroke="var(--orange)" stroke-width="10"/>
    <path d="M200,0 C240,100 240,220 208,320 L0,320 L0,0 Z" fill="var(--white)"/>
  </svg>
  <div class="contact">
    <p class="contact__name">Lorcan Whitlaney</p>
    <p class="contact__role">Foreman</p>
    <p class="contact__area">Servicing North Jersey</p>
    <ul class="contact__list">
      <li>(T)1-888-555-0142<svg class="icon"><use href="#icon-phone"/></svg></li>
      <li>201-555-0187<svg class="icon"><use href="#icon-phone"/></svg></li>
      <li>info@Kestrel-Line.com<svg class="icon"><use href="#icon-at"/></svg></li>
      <li>www.Kestrel-Line.com<svg class="icon"><use href="#icon-web"/></svg></li>
    </ul>
    <p class="contact__special">Specializing in :</p>
    <p class="contact__trades">roofs / chimneys / masonry / gutters</p>
  </div>
  <div class="brand">
    <p class="brand__name">KestrelLine<br>Construction</p>
    <p class="brand__tagline">Residential &amp; Commercial... 24hr emergency service.</p>
  </div>
</section>

</body>
</html>
```